Create custom funnel illustration

I've attached 3 files to this project. One is an example of the current design/colors so I'm looking for a design to match the current look & feel.

Second is a section of the website that we want to replace with the new infographic design.

Lastly, is a sample concept of what we're looking for.

Target Market(s)

40+ college educated

Industry/Entity Type

Business Software

Font styles to use
Sans Serif

Requirements
Must have
• Design to match the current look & feel. See "design-sample.png"

```html
<!DOCTYPE html>
<html lang="en">
<head>
<meta charset="utf-8">
<title>Modern Trust Funnel</title>
<link rel="stylesheet" href="https://fonts.googleapis.com/css2?family=Poppins:wght@300;400;700&display=swap">
<style>
  :root {
    --purple: #6a52ad;
    --sky: #52b5e8;
    --funnel-grey: #cfcfcf;
    --frame-line: #d9d9d9;
    --ink: #111111;
    --paper: #ffffff;
  }
  html, body {
    margin: 0;
    padding: 0;
    width: 1200px;
    height: 1200px;
    overflow: hidden;
    background: var(--paper);
  }
  .canvas {
    display: block;
    width: 1200px;
    height: 1200px;
    font-family: "Poppins", sans-serif;
  }
  .frame { fill: var(--paper); stroke: var(--frame-line); stroke-width: 1; }
  .funnel { fill: var(--funnel-grey); }
  .flow-line { fill: none; stroke: var(--purple); stroke-width: 1.3; }
  .arrow-head { fill: var(--purple); }
  .icon-slot { fill: var(--purple); opacity: 0.85; }
  .icon-slot--sky { fill: var(--sky); }
  .asset-label { font-size: 17.5px; fill: var(--ink); font-weight: 300; text-anchor: middle; }
  .asset-label .strong { font-weight: 700; }
  .trust-title { font-size: 28.5px; fill: var(--ink); font-weight: 300; text-anchor: middle; }
  .trust-title .strong { font-weight: 700; }
  .beneficiaries { font-size: 26px; fill: var(--ink); font-weight: 300; text-anchor: middle; }
  .beneficiaries .strong { font-weight: 700; }
</style>
</head>
<body>
<svg class="canvas" viewBox="0 0 1200 1200" xmlns="http://www.w3.org/2000/svg">
  <defs>
    <marker id="arrowhead" viewBox="0 0 10 10" refX="9" refY="5" markerWidth="7" markerHeight="7" orient="auto-start-reverse">
      <path class="arrow-head" d="M0,0 L10,5 L0,10 z"/>
    </marker>
  </defs>

  <rect class="frame" x="256.5" y="101.5" width="700" height="788"/>

  <path class="funnel" d="M361,489 H854 L664,675 Q652,688 652,700 V802 Q652,812 642,809 L572,787 Q564,783 564,775 V700 Q564,688 552,675 Z"/>

  <polyline class="flow-line" points="368,359 391,359 391,497 433,539" marker-end="url(#arrowhead)"/>
  <polyline class="flow-line" points="586,256 612,256 612,373" marker-end="url(#arrowhead)"/>
  <polyline class="flow-line" points="561,372 561,525" marker-end="url(#arrowhead)"/>
  <polyline class="flow-line" points="669,361 729,361 729,526" marker-end="url(#arrowhead)"/>
  <polyline class="flow-line" points="443,487 503,487 503,556" marker-end="url(#arrowhead)"/>
  <polyline class="flow-line" points="614,482 674,482 674,527" marker-end="url(#arrowhead)"/>
  <polyline class="flow-line" points="801,480 801,519 753,567" marker-end="url(#arrowhead)"/>

  <rect class="icon-slot" x="552" y="153" width="71" height="69" rx="4" role="img" aria-label="Businessman with briefcase standing on a ledge"/>
  <rect class="icon-slot" x="371" y="244" width="72" height="76" rx="4" role="img" aria-label="Person relaxing in a rocking chair"/>
  <rect class="icon-slot" x="502" y="266" width="64" height="71" rx="4" role="img" aria-label="Rising bar chart with a coin and growth arrow"/>
  <rect class="icon-slot" x="674" y="237" width="60" height="87" rx="4" role="img" aria-label="House outline with a person at the door"/>
  <rect class="icon-slot" x="428" y="384" width="89" height="69" rx="4" role="img" aria-label="Bank building with a coin on the roof"/>
  <rect class="icon-slot" x="608" y="386" width="72" height="61" rx="4" role="img" aria-label="House with a price tag"/>
  <rect class="icon-slot" x="747" y="366" width="98" height="82" rx="4" role="img" aria-label="Open umbrella above a ledge"/>
  <rect class="icon-slot icon-slot--sky" x="573" y="730" width="70" height="75" rx="4" role="img" aria-label="Group of three people standing together"/>

  <text class="asset-label" x="589" y="245"><tspan class="strong">Business</tspan> interests</text>
  <text class="asset-label" x="404" y="345"><tspan class="strong">Retirement</tspan></text>
  <text class="asset-label" x="533" y="359"><tspan class="strong">Stock</tspan> market</text>
  <text class="asset-label" x="709" y="347"><tspan class="strong">Personal</tspan> property</text>
  <text class="asset-label" x="474" y="474"><tspan class="strong">Bank</tspan> accounts</text>
  <text class="asset-label" x="647" y="469"><tspan class="strong">Real estate</tspan></text>
  <text class="asset-label" x="803" y="471"><tspan class="strong">Insurance</tspan></text>

  <text class="trust-title" x="607" y="584"><tspan class="strong">Your</tspan></text>
  <text class="trust-title" x="607" y="618">modern</text>
  <text class="trust-title" x="607" y="652">Trust</text>

  <text class="beneficiaries" x="608" y="836">Trust <tspan class="strong">Beneficiaries</tspan></text>
</svg>
</body>
</html>
```